Crafted Ember Website

Would like a website designed for my fitness and nutrition coaching company Craft Ember. I have a company logo and would like to keep the page layout clean and simple. Needs to look great on computer and mobile devices.

Target Market(s)

Target market is individuals looking to make changes in their health and nutrition with the help of an online coach.

Industry/Entity Type

Fitness

Number of Pages Required

2 page

Colors
3176b5
0355a3
85acd3
cedeed
f8fcfd
ffffff

Requirements
Must have
• The first page should have the company logo and name towards the top and below that client before and after photos scrolling or displaying in some manner. Also would like a section that states services offered and a section about myself since I am the primary coach for clients.

```html
<!DOCTYPE html>
<html lang="en">
<head>
<meta charset="utf-8">
<title>Crafted Ember – Fitness & Nutrition Coaching</title>
<link rel="stylesheet" href="https://fonts.googleapis.com/css2?family=Raleway:wght@400;500;600&family=Open+Sans:wght@400;600&display=swap">
<style>
:root{
  --blue:#3176b5;
  --blue-deep:#0355a3;
  --blue-soft:#85acd3;
  --blue-pale:#cedeed;
  --ice:#f8fcfd;
  --white:#ffffff;
  --ink:#333a40;
  --text:#555c63;
  --grey:#5a5d61;
  --grey-dark:#45484c;
  --footer:#1b1c1e;
  --footer-bar:#111213;
}
*{box-sizing:border-box;margin:0;padding:0}
html,body{width:1200px;height:4675px;overflow:hidden}
body{background:var(--white);font-family:"Open Sans",Arial,sans-serif;color:var(--text);position:relative}
.abs{position:absolute}
.heading{font-family:"Raleway",Arial,sans-serif;font-weight:500;letter-spacing:1px}
.lead{font-size:14px;line-height:22px;color:var(--text)}
.btn{position:absolute;display:flex;align-items:center;justify-content:center;font-family:"Raleway",Arial,sans-serif;font-size:17px;font-weight:500;color:var(--white);letter-spacing:.5px}
.ph{position:absolute}

/* header */
.site-header{position:absolute;top:0;left:0;width:1200px;height:140px;background:var(--white);z-index:3}
.callbar{position:absolute;right:0;top:0;width:470px;height:47px;background:var(--grey);clip-path:polygon(8% 0,100% 0,100% 100%,0 100%);display:flex;align-items:center;justify-content:flex-end;padding-right:48px;gap:12px;color:var(--white);font-size:16px}
.callbar .num{font-size:19px;font-weight:600;letter-spacing:1px}
.phone-dot{width:30px;height:30px;border-radius:50%;background:var(--white);display:flex;align-items:center;justify-content:center}
.brand{position:absolute;left:78px;top:104px;width:252px;text-align:center}
.brand .name{font-family:"Raleway",Arial,sans-serif;font-weight:600;font-size:24px;line-height:30px;color:var(--blue-deep);letter-spacing:1px}
.main-nav{position:absolute;left:465px;top:82px;display:flex}
.main-nav a{display:block;padding:12px 16px;font-family:"Raleway",Arial,sans-serif;font-size:15px;font-weight:500;color:var(--ink);text-decoration:none}
.main-nav a.active{background:var(--blue);color:var(--white)}

/* hero */
.hero{position:absolute;top:140px;left:0;width:1200px;height:540px;overflow:hidden}
.hero-bg{position:absolute;inset:0;background:linear-gradient(90deg,#d9d3cc 0%,#eae7e3 35%,#f0f0ef 65%,#c9cdd2 100%)}
.hero-title{position:absolute;top:202px;left:0;width:1200px;text-align:center}
.hero-title .name{font-family:"Raleway",Arial,sans-serif;font-size:34px;line-height:40px;font-weight:500;color:var(--ink);letter-spacing:1px}
.hero-title h1{font-family:"Raleway",Arial,sans-serif;font-size:54px;line-height:62px;font-weight:500;color:var(--blue);margin-top:4px}

/* welcome */
.welcome h2{position:absolute;top:795px;width:1200px;text-align:center;font-size:38px;color:var(--blue-deep)}
.welcome h2 span{color:var(--ink)}
.welcome .lead{position:absolute;top:852px;left:150px;width:900px;text-align:center}

/* services */
.services{position:absolute;top:1247px;left:0;width:1200px;height:679px;background:linear-gradient(180deg,#2f74b5 0%,#1f68ae 55%,#2a70b2 100%)}
.services h2{position:absolute;top:170px;width:1200px;text-align:center;color:var(--white);font-size:38px}
.services h2 span{color:var(--blue-soft)}
.card{position:absolute;top:255px;width:320px;height:353px;background:var(--white)}
.card .ph{left:0;top:0;width:320px;height:198px}
.card .badge{position:absolute;left:138px;top:172px;width:44px;height:44px;border-radius:50%;background:var(--white);border:3px solid var(--blue-deep)}
.card h3{position:absolute;top:250px;width:100%;text-align:center;font-family:"Raleway",Arial,sans-serif;font-size:17px;font-weight:600;color:var(--blue-deep);letter-spacing:.5px}
.card p{position:absolute;top:283px;left:30px;width:260px;text-align:center;font-size:13px;line-height:21px}

/* testimonials */
.testimonials{position:absolute;top:1926px;left:0;width:1200px;height:256px;background:var(--grey)}
.testimonials .label{position:absolute;left:0;top:0;width:374px;height:256px;background:var(--grey-dark)}
.testimonials h2{position:absolute;left:87px;top:98px;color:var(--white);font-size:36px}
.testimonials .sub{position:absolute;left:112px;top:145px;color:#e6e6e6;font-size:14px}
.testimonials .quote{position:absolute;left:560px;top:64px;width:550px;font-size:14px;line-height:24px;color:#f0f0f0}
.testimonials .client{position:absolute;left:560px;top:165px;color:var(--white);font-family:"Raleway",Arial,sans-serif;font-weight:600;font-size:15px;letter-spacing:1px}
.dots{position:absolute;left:1006px;top:184px;display:flex;gap:8px}
.dots i{width:14px;height:14px;border-radius:50%;border:2px solid #d8d8d8}
.dots i.on{background:var(--blue-soft);border-color:var(--blue-soft)}

/* about */
.about h2{position:absolute;left:78px;top:2255px;font-size:38px;color:var(--blue-deep)}
.about .lead{position:absolute;left:78px;width:590px}

/* gallery */
.gallery-top{position:absolute;top:2650px;left:0;width:1200px;height:187px;background:linear-gradient(180deg,#3a7cba,#2a6fb1)}
.gallery h2{position:absolute;top:2752px;width:1200px;text-align:center;color:var(--white);font-size:38px}
.gallery h2 span{color:var(--blue-soft)}
.gallery-bottom{position:absolute;top:3382px;left:0;width:1200px;height:196px;background:linear-gradient(180deg,#2b70b2,#3b7dba)}
.ghost-btn{position:absolute;left:467px;top:3457px;width:266px;height:56px;border:2px solid var(--white);display:flex;align-items:center;justify-content:center;color:var(--white);font-family:"Raleway",Arial,sans-serif;font-size:17px;letter-spacing:1px}

/* contact */
.contact h2{position:absolute;top:3630px;width:1200px;text-align:center;font-size:38px;color:var(--blue-deep)}
.contact .lead{position:absolute;top:3690px;left:200px;width:800px;text-align:center}
.contact .ask{position:absolute;top:3750px;width:1200px;text-align:center;font-family:"Raleway",Arial,sans-serif;font-weight:600;font-size:18px;color:var(--blue-deep)}
.form-box{position:absolute;left:193px;top:3809px;width:811px;height:343px;background:var(--white);border:2px solid #e2e4e6}
.field{position:absolute;background:#ececec;font-size:13px;color:#777;padding:13px 16px}
.submit{position:absolute;left:41px;top:227px;width:736px;height:56px;background:var(--blue);color:var(--white);font-family:"Raleway",Arial,sans-serif;font-size:17px;display:flex;align-items:center;justify-content:center;letter-spacing:1px}

/* newsletter */
.newsletter{position:absolute;top:4224px;left:0;width:1200px;height:102px;background:var(--blue)}
.newsletter h2{position:absolute;left:78px;top:32px;color:var(--white);font-size:31px;line-height:38px;letter-spacing:1px}
.nl-input{position:absolute;top:30px;height:46px;border:2px solid var(--white);color:var(--white);font-size:13px;padding:12px 16px}
.nl-btn{position:absolute;left:929px;top:30px;width:193px;height:46px;background:var(--white);color:var(--blue-deep);font-family:"Raleway",Arial,sans-serif;font-size:17px;font-weight:600;display:flex;align-items:center;justify-content:center;letter-spacing:1px}

/* footer */
.footer{position:absolute;top:4326px;left:0;width:1200px;height:287px;background:var(--footer);color:#cfd2d5}
.footer .brand-foot{position:absolute;left:60px;top:128px;width:286px;text-align:center}
.footer .brand-foot .name{font-family:"Raleway",Arial,sans-serif;font-weight:600;font-size:24px;line-height:30px;color:var(--white);letter-spacing:1px}
.socials{position:absolute;left:115px;top:200px;display:flex;gap:18px}
.socials i{width:40px;height:40px;border-radius:50%;background:var(--blue)}
.foot-col h4{position:absolute;top:40px;font-family:"Raleway",Arial,sans-serif;font-size:16px;font-weight:600;color:var(--blue-soft);letter-spacing:1px}
.sitemap{position:absolute;left:343px;top:80px;list-style:none}
.sitemap li{font-size:13px;line-height:31px;color:#e6e6e6;padding-left:16px;position:relative}
.sitemap li::before{content:"";position:absolute;left:0;top:13px;width:5px;height:5px;border-radius:50%;background:var(--blue-soft)}
.foot-quote{position:absolute;left:570px;top:84px;width:250px;font-size:13px;line-height:24px}
.foot-name{position:absolute;left:570px;top:168px;font-size:14px;color:var(--blue-soft)}
.arrows{position:absolute;left:570px;top:200px;display:flex;gap:8px}
.arrows i{width:36px;height:36px;background:var(--blue);display:flex;align-items:center;justify-content:center}
.contact-line{position:absolute;left:866px;display:flex;gap:16px;font-size:13px;line-height:22px;color:#e6e6e6}
.contact-line svg{flex:none;margin-top:2px}
.copy{position:absolute;top:4613px;left:0;width:1200px;height:62px;background:var(--footer-bar);display:flex;align-items:center;justify-content:center;font-size:13px;color:var(--blue-soft)}
</style>
</head>
<body>

<header class="site-header">
  <div class="callbar">
    <span>Call Us Today :</span>
    <span class="phone-dot"><svg width="16" height="16" viewBox="0 0 24 24"><path fill="#5a5d61" d="M6.6 10.8a15.1 15.1 0 0 0 6.6 6.6l2.2-2.2c.3-.3.7-.4 1-.2 1.1.4 2.3.6 3.6.6.6 0 1 .4 1 1V20c0 .6-.4 1-1 1A17 17 0 0 1 3 4c0-.6.4-1 1-1h3.5c.6 0 1 .4 1 1 0 1.3.2 2.5.6 3.6.1.3 0 .7-.2 1z"/></svg></span>
    <span class="num">123 - 456 - 7890</span>
  </div>
  <div class="brand">
    <div class="name">CRAFTED EMBER</div>
  </div>
  <nav class="main-nav">
    <a class="active">HOME</a><a>ABOUT</a><a>SERVICES</a><a>GALLERY</a><a>TESTIMONIAL</a><a>CONTACT</a>
    <a><svg width="18" height="18" viewBox="0 0 24 24"><circle cx="10" cy="10" r="7" fill="none" stroke="#3176b5" stroke-width="3"/><path d="M15 15l6 6" stroke="#3176b5" stroke-width="3"/></svg></a>
  </nav>
</header>

<section class="hero">
  <div class="hero-bg"></div>
  <div class="ph" role="img" aria-label="Smiling woman eating a fresh salad" style="left:0;top:0;width:440px;height:540px;background:linear-gradient(135deg,#c8b6a6,#e3d6c8 55%,#d9e0c2)"></div>
  <div class="ph" role="img" aria-label="Fit woman in sportswear holding a dumbbell" style="left:820px;top:0;width:380px;height:540px;background:linear-gradient(200deg,#b5bfca,#d8c2b2 55%,#6f9ccc)"></div>
  <div class="hero-title">
    <div class="name">CRAFTED EMBER</div>
    <h1>Are You Ready To Change?</h1>
  </div>
  <div class="btn" style="left:390px;top:352px;width:202px;height:56px;background:var(--blue)">JOIN US NOW</div>
  <div class="btn" style="left:608px;top:352px;width:202px;height:56px;background:var(--grey)">CONTACT US</div>
  <svg class="abs" style="left:0;top:440px" width="1200" height="100" viewBox="0 0 1200 100" preserveAspectRatio="none">
    <path d="M0 45 Q600 110 1200 45 L1200 100 L0 100Z" fill="#ffffff"/>
    <path d="M0 40 Q600 105 1200 40" fill="none" stroke="#3176b5" stroke-width="5"/>
  </svg>
</section>

<section class="welcome">
  <h2 class="heading">WELCOME TO <span>CRAFTED EMBER</span></h2>
  <p class="lead">Lorem Ipsum is simply dummy text of the printing and typesetting industry. Lorem Ipsum has been the industry's standard dummy text ever since the 1500s, when an unknown printer took a galley of type and scrambled it to make a type specimen book.It has survived not only five centuries, but also the leap into electronic typesetting.</p>
  <div class="ph" role="img" aria-label="Client before and after photos side by side" style="left:78px;top:975px;width:299px;height:272px;background:linear-gradient(90deg,#cfd6de,#b89c8c 50%,#d8dde3)"></div>
  <div class="ph" role="img" aria-label="Client before and after transformation on blue background" style="left:449px;top:975px;width:299px;height:272px;background:linear-gradient(90deg,#3f79b3,#5d8fbf 50%,#3f79b3)"></div>
  <div class="ph" role="img" aria-label="Client before and after photos in yellow sportswear" style="left:820px;top:975px;width:302px;height:272px;background:linear-gradient(90deg,#c79c82,#d7b08f 50%,#c49880)"></div>
</section>

<section class="services">
  <svg class="abs" style="left:0;top:0" width="1200" height="90" viewBox="0 0 1200 90"><path d="M0 0 L0 20 L600 80 L1200 20 L1200 0Z" fill="#ffffff"/></svg>
  <svg class="abs" style="left:565px;top:34px" width="70" height="60" viewBox="0 0 70 60">
    <circle cx="24" cy="38" r="9" fill="none" stroke="#45484c" stroke-width="6"/>
    <circle cx="46" cy="20" r="8" fill="none" stroke="#3176b5" stroke-width="5"/>
  </svg>
  <h2 class="heading">OUR BEST <span>SERVICES</span></h2>
  <article class="card" style="left:78px">
    <div class="ph" role="img" aria-label="Group fitness class exercising" style="background:linear-gradient(135deg,#7fa8c8,#d6a796 60%,#9ec3dc)"></div>
    <div class="badge"></div>
    <h3>FITNESS TRAINING</h3>
    <p>Lorem Ipsum is simply dummy text of the printing and typesetting industry.</p>
  </article>
  <article class="card" style="left:440px">
    <div class="ph" role="img" aria-label="Man lifting kettlebells in a gym" style="background:linear-gradient(135deg,#5d6670,#9aa3ad 55%,#c1c6cc)"></div>
    <div class="badge"></div>
    <h3>NUTRITION TRANING</h3>
    <p>Lorem Ipsum is simply dummy text of the printing and typesetting industry.</p>
  </article>
  <article class="card" style="left:801px">
    <div class="ph" role="img" aria-label="Supplement capsules next to fresh broccoli" style="background:linear-gradient(135deg,#d8d3bd,#8fb05c 60%,#5f8f3a)"></div>
    <div class="badge"></div>
    <h3>SUPPLEMENTS</h3>
    <p>Lorem Ipsum is simply dummy text of the printing and typesetting industry.</p>
  </article>
</section>

<section class="testimonials">
  <div class="label"></div>
  <h2 class="heading">TESTIMONIALS</h2>
  <div class="sub">What Our Client Say</div>
  <div class="ph" role="img" aria-label="Portrait of a client" style="left:390px;top:60px;width:140px;height:136px;background:linear-gradient(180deg,#e4e7ea,#b9c2cb);border:3px solid #fff"></div>
  <p class="quote">" Lorem Ipsum is simply dummy text of the printing and typesetting industry. Lorem Ipsum has been the industry's standard dummy text ever since the 1500s, when an unknown printer took a galley of type and scrambled it "</p>
  <div class="client">— CLIENT NAME</div>
  <div class="dots"><i class="on"></i><i></i><i></i><i></i><i></i></div>
  <svg class="abs" style="left:555px;top:256px" width="90" height="44" viewBox="0 0 90 44"><path d="M0 0 L90 0 L45 44Z" fill="#5a5d61"/></svg>
</section>

<section class="about">
  <h2 class="heading">ABOUT ME</h2>
  <p class="lead" style="top:2318px">Lorem Ipsum is simply dummy text of the printing and typesetting industry. Lorem Ipsum has been the industry's standard dummy text ever since the 1500s, when an unknown printer took a galley of type and scrambled it to make a type specimen book.</p>
  <p class="lead" style="top:2412px">It has survived not only five centuries, but also the leap into electronic typesetting, remaining essentially unchanged. It was popularised in the 1960s with the release of Letraset sheets containing Lorem Ipsum passages, and more recently with desktop publishing software like Aldus PageMaker including versions of Lorem Ipsum.</p>
  <div class="btn" style="left:78px;top:2537px;width:184px;height:56px;background:var(--blue)">CONTACT US</div>
  <div class="ph" role="img" aria-label="Dumbbells, green apple and measuring tape" style="left:700px;top:2244px;width:438px;height:390px;background:radial-gradient(circle at 45% 55%,#9ccb4a 0 22%,#ffffff 45%),#fff"></div>
</section>

<section class="gallery">
  <div class="gallery-top"></div>
  <svg class="abs" style="left:565px;top:2640px" width="70" height="60" viewBox="0 0 70 60">
    <rect x="12" y="14" width="46" height="34" fill="none" stroke="#45484c" stroke-width="5"/>
    <path d="M16 44 L30 28 L40 38 L46 32 L55 44Z" fill="#45484c"/>
  </svg>
  <h2 class="heading">OUR <span>GALLERY</span></h2>
  <div class="ph" role="img" aria-label="Group running outdoors" style="left:0;top:2837px;width:300px;height:272px;background:linear-gradient(135deg,#8aa5b5,#4f6f8a)"></div>
  <div class="ph" role="img" aria-label="Woman stretching on a mat" style="left:300px;top:2837px;width:300px;height:272px;background:linear-gradient(135deg,#eef1f3,#c8ced6)"></div>
  <div class="ph" role="img" aria-label="Woman eating a healthy salad" style="left:600px;top:2837px;width:300px;height:272px;background:linear-gradient(135deg,#d9b49b,#9cbf6a)"></div>
  <div class="ph" role="img" aria-label="Woman doing a yoga pose" style="left:900px;top:2837px;width:300px;height:272px;background:linear-gradient(135deg,#e9eaec,#5e6166)"></div>
  <div class="ph" role="img" aria-label="Woman jogging in sportswear" style="left:0;top:3109px;width:300px;height:273px;background:linear-gradient(135deg,#9fb7c7,#c86d7f)"></div>
  <div class="ph" role="img" aria-label="Close up of running shoes" style="left:300px;top:3109px;width:300px;height:273px;background:linear-gradient(135deg,#b7c0c8,#7f8b95)"></div>
  <div class="ph" role="img" aria-label="Woman drinking water in the city" style="left:600px;top:3109px;width:300px;height:273px;background:linear-gradient(135deg,#e4dfd6,#8db3c6)"></div>
  <div class="ph" role="img" aria-label="Smiling woman in workout gear" style="left:900px;top:3109px;width:300px;height:273px;background:linear-gradient(135deg,#cfb3a3,#6d7a86)"></div>
  <div class="gallery-bottom"></div>
  <div class="ghost-btn">VIEW ALL GALLERY</div>
</section>

<section class="contact">
  <div class="ph" role="img" aria-label="Glass of orange juice with fresh greens" style="left:0;top:3755px;width:171px;height:400px;background:linear-gradient(180deg,#f6f6f4,#f3c54a 55%,#7ca552)"></div>
  <div class="ph" role="img" aria-label="Fit woman holding a dumbbell" style="left:1004px;top:3600px;width:196px;height:624px;background:linear-gradient(180deg,#f3e6d8,#d7b39b 45%,#8fd0cf)"></div>
  <h2 class="heading">CONTACT US</h2>
  <p class="lead">Lorem Ipsum is simply dummy text of the printing and typesetting industry. Lorem Ipsum has been the industry's standard dummy text ever since the 1500s, when an unknown printer took a galley.</p>
  <div class="ask">Need a Free Quote or have a question? &nbsp;Get in touch</div>
  <form class="form-box">
    <div class="field" style="left:41px;top:59px;width:306px;height:46px">Name *</div>
    <div class="field" style="left:41px;top:117px;width:306px;height:46px">Email *</div>
    <div class="field" style="left:41px;top:174px;width:306px;height:46px">Phone *</div>
    <div class="field" style="left:365px;top:59px;width:412px;height:160px">Message *</div>
    <div class="submit">SUBMIT</div>
  </form>
</section>

<section class="newsletter">
  <h2 class="heading">NEWSLETTER</h2>
  <div class="nl-input" style="left:327px;width:287px">Enter Name *</div>
  <div class="nl-input" style="left:627px;width:289px">Enter Email *</div>
  <div class="nl-btn">SUBSCRIBE</div>
</section>

<footer class="footer">
  <div class="brand-foot">
    <div class="name">CRAFTED EMBER</div>
  </div>
  <div class="socials"><i></i><i></i><i></i></div>
  <div class="foot-col"><h4 style="left:343px">SITEMAP</h4></div>
  <ul class="sitemap"><li>Home</li><li>About</li><li>Services</li><li>Gallery</li><li>Testimonials</li><li>Contact Us</li></ul>
  <div class="foot-col"><h4 style="left:570px">CLIENT TESTIMONIALS</h4></div>
  <p class="foot-quote">" Lorem Ipsum is simply dummy text of the printing and typesetting indu Lorem Ipsum has been the. "</p>
  <div class="foot-name">— Client Name</div>
  <div class="arrows">
    <i><svg width="12" height="14"><path d="M9 1 L3 7 L9 13" stroke="#fff" stroke-width="2.5" fill="none"/></svg></i>
    <i><svg width="12" height="14"><path d="M3 1 L9 7 L3 13" stroke="#fff" stroke-width="2.5" fill="none"/></svg></i>
  </div>
  <div class="foot-col"><h4 style="left:866px">CONTACT US</h4></div>
  <div class="contact-line" style="top:80px">
    <svg width="18" height="22" viewBox="0 0 18 22"><path d="M9 0a8 8 0 0 1 8 8c0 6-8 14-8 14S1 14 1 8a8 8 0 0 1 8-8z" fill="#3176b5"/><circle cx="9" cy="8" r="3" fill="#1b1c1e"/></svg>
    <div><b style="font-weight:600">CRAFTED EMBER</b><br>101 - Lorem ipsum is the<br>text simple dummy</div>
  </div>
  <div class="contact-line" style="top:170px">
    <svg width="18" height="18" viewBox="0 0 24 24"><path fill="#3176b5" d="M6.6 10.8a15.1 15.1 0 0 0 6.6 6.6l2.2-2.2c.3-.3.7-.4 1-.2 1.1.4 2.3.6 3.6.6.6 0 1 .4 1 1V20c0 .6-.4 1-1 1A17 17 0 0 1 3 4c0-.6.4-1 1-1h3.5c.6 0 1 .4 1 1 0 1.3.2 2.5.6 3.6.1.3 0 .7-.2 1z"/></svg>
    <div>123 - 456 - 7890</div>
  </div>
  <div class="contact-line" style="top:216px">
    <svg width="18" height="16" viewBox="0 0 18 14"><rect width="18" height="14" fill="#3176b5"/><path d="M0 0 L9 8 L18 0" stroke="#1b1c1e" stroke-width="1.5" fill="none"/></svg>
    <div>info@craftedember.com</div>
  </div>
</footer>
<div class="copy">CRAFTED EMBER - 2017 All Right Reserved</div>

</body>
</html>
```